Brand design for Varundel Partners

We are a new start up Fund Manager based in Singapore in need of a stylish and slick corporate identity starting with letterhead and business card (2 separate projects on craft hive but must be completed as one). We are aiming to be a somewhat 'budget' service provider with a target market of high net worth individuals and savvy self traders so we need to have our look convey value but with style. Our logo is attached and the use of the blue is imperative. The company name is Varundel Partners Pte Ltd and the verbiage 'Licensed by the Financial Oversight Board of Singapore - RFMC licence no. QRT804217-3' should be incorporated in small print.

Business card should also include address, office, direct and mobile numbers as well as email address. Follow me on twitter/fb/linkedin/Google+ should also be incrorporated. We are also looking to have a QR code on the business card that people can read with a smartphone which will auto populate our contact details in to their address book.

Many thanks and happy designing!

Reason: Extending so we can have further internal discussions. Thanks for input so far, some great designs coming through! Cheers

```html
<!DOCTYPE html>
<html lang="en">
<head>
<meta charset="utf-8">
<title>Varundel Partners – Stationery Suite</title>
<link rel="stylesheet" href="https://fonts.googleapis.com/css2?family=Mulish:ital,wght@0,400;0,600;0,700;1,400;1,600&display=swap">
<style>
  :root {
    --bg: #f1f1f1;
    --paper: #ffffff;
    --blue-deep: #2a5499;
    --blue: #3470b4;
    --blue-light: #4a9bd8;
    --slate: #868b98;
    --ink: #3a3a3a;
    --muted: #8a8a8a;
  }
  * { box-sizing: border-box; margin: 0; padding: 0; }
  html, body { width: 1200px; height: 1000px; overflow: hidden; }
  body { background: var(--bg); font-family: "Mulish", Arial, sans-serif; color: var(--ink); position: relative; }

  .sheet { position: absolute; background: var(--paper); overflow: hidden; }
  .brand-name { color: var(--blue-deep); font-weight: 700; letter-spacing: 0.2px; white-space: nowrap; }
  .brand-name.on-blue { color: #ffffff; }

  .base-strip { position: absolute; left: 0; right: 0; bottom: 0; height: 5px;
    background: linear-gradient(100deg, var(--slate) 0 38%, var(--paper) 38% 39%, var(--blue-light) 39% 48%, var(--blue-deep) 48% 100%); }

  .blue-field { position: absolute; inset: 0; background: linear-gradient(180deg, var(--blue-deep) 0%, var(--blue) 60%, #3d8ccb 100%); }
  .ridge { position: absolute; left: 0; bottom: 0; width: 100%; }

  .tiny { font-size: 4px; line-height: 5.5px; color: var(--muted); }
  .small { font-size: 5px; line-height: 6.5px; color: var(--ink); }
  .accent { color: var(--blue-deep); font-weight: 700; }

  /* Letterhead */
  .letterhead { left: 292px; top: 98px; width: 294px; height: 416px; }
  .letterhead .brand-name { position: absolute; right: 30px; top: 36px; font-size: 15px; }
  .letterhead .salutation { position: absolute; left: 21px; top: 101px; font-size: 7px; font-weight: 700; }
  .letterhead .body { position: absolute; left: 21px; top: 116px; width: 254px; }
  .letterhead .body p { font-size: 4.6px; line-height: 6.6px; color: #555; text-align: justify; margin-bottom: 6.5px; }
  .letterhead .closing { position: absolute; right: 21px; top: 307px; text-align: right; }
  .letterhead .closing .regards { font-size: 4.6px; color: #666; }
  .letterhead .closing .signer { font-size: 6.5px; font-weight: 700; margin-top: 4px; }
  .letterhead .signature { position: absolute; left: 150px; top: 302px; width: 78px; height: 30px;
    background: linear-gradient(90deg, #e6ebf5, #d6def0); border-radius: 3px; }
  .letterhead .foot-left { position: absolute; left: 21px; top: 386px; }
  .letterhead .foot-right { position: absolute; right: 21px; top: 386px; text-align: right; }

  /* Folder */
  .folder { left: 636px; top: 80px; width: 346px; height: 437px; }
  .folder .brand-name { position: absolute; left: 142px; top: 72px; font-size: 21px; }

  /* Business cards */
  .card-front { left: 186px; top: 549px; width: 133px; height: 77px; }
  .card-front .brand-name { position: absolute; left: 8px; top: 16px; font-size: 9px; }
  .card-front .person { position: absolute; right: 10px; top: 22px; text-align: right; }
  .card-front .person .name { font-size: 5px; font-weight: 700; color: var(--blue-deep); }
  .card-front .address { position: absolute; left: 8px; top: 54px; }
  .card-front .contact { position: absolute; right: 10px; top: 54px; text-align: right; }
  .card-front .base-strip { height: 4px; }
  .card-back { left: 186px; top: 647px; width: 133px; height: 74px; }
  .card-back .brand-name { position: absolute; left: 34px; top: 19px; font-size: 9px; }

  /* DL letter */
  .dl-letter { left: 353px; top: 561px; width: 328px; height: 157px; }
  .dl-letter .brand-name { position: absolute; left: 24px; top: 34px; font-size: 15px; }
  .dl-letter .foot-left { position: absolute; left: 24px; top: 126px; }
  .dl-letter .foot-right { position: absolute; right: 24px; top: 126px; text-align: right; }

  /* Envelope */
  .envelope { left: 713px; top: 561px; width: 328px; height: 157px; }
  .envelope .flap { position: absolute; left: 0; top: 0; width: 100%; height: 84px;
    background: linear-gradient(90deg, var(--blue-deep) 0%, var(--blue) 60%, #4688c6 100%); }
  .envelope .brand-name { position: absolute; left: 146px; top: 21px; font-size: 6.5px; }

  /* CD sleeve & disc */
  .cd-sleeve { left: 243px; top: 772px; width: 195px; height: 176px; }
  .cd-sleeve .brand-name { position: absolute; left: 32px; top: 44px; font-size: 14px; }
  .cd-disc { position: absolute; left: 471px; top: 776px; width: 168px; height: 168px; }

  /* Compliments slip */
  .compliments { left: 742px; top: 773px; width: 299px; height: 140px; }
  .compliments .brand-name { position: absolute; left: 18px; top: 23px; font-size: 13px; }
  .compliments .greeting { position: absolute; right: 17px; top: 33px; font-size: 11px; font-style: italic; color: var(--slate); }
  .compliments .greeting b { color: var(--blue-deep); font-weight: 600; }
  .compliments .foot-left { position: absolute; left: 18px; top: 120px; }
  .compliments .foot-right { position: absolute; right: 17px; top: 110px; text-align: right; }
</style>
</head>
<body>

<!-- Letterhead -->
<section class="sheet letterhead">
  <div class="brand-name">Varundel Partners</div>
  <p class="salutation">Dear sir / madame,</p>
  <div class="body">
    <p>Lorem ipsum dolor sit amet, consectetur adipisicing elit, sed do eiusmod tempor incididunt ut labore et dolore magna aliqua. Ut enim ad minim veniam, quis nostrud exercitation ullamco laboris nisi ut aliquip ex ea commodo consequat. Duis aute irure dolor in reprehenderit in voluptate velit esse cillum dolore eu fugiat nulla pariatur. Excepteur sint occaecat cupidatat non proident, sunt in culpa qui officia deserunt mollit anim id est laborum. Lorem ipsum dolor sit amet, consectetur adipisicing elit, sed do eiusmod tempor incididunt ut labore et dolore magna aliqua. Ut enim ad minim veniam, quis nostrud exercitation ullamco laboris nisi ut aliquip ex ea commodo consequat. Duis aute irure dolor in reprehenderit in voluptate velit esse cillum dolore eu fugiat nulla pariatur. Excepteur sint occaecat cupidatat non proident, sunt in culpa qui officia deserunt mollit anim id est laborum.</p>
    <p>Lorem ipsum dolor sit amet, consectetur adipisicing elit, sed do eiusmod tempor incididunt ut labore et dolore magna aliqua. Ut enim ad minim veniam, quis nostrud exercitation ullamco laboris nisi ut aliquip ex ea commodo consequat. Duis aute irure dolor in reprehenderit in voluptate velit esse cillum dolore eu fugiat nulla pariatur. Excepteur sint occaecat cupidatat non proident, sunt in culpa qui officia deserunt mollit anim id est laborum.</p>
    <p>Lorem ipsum dolor sit amet, consectetur adipisicing elit, sed do eiusmod tempor incididunt ut labore et dolore magna aliqua. Ut enim ad minim veniam, quis nostrud exercitation ullamco laboris nisi ut aliquip ex ea commodo consequat. Duis aute irure dolor in reprehenderit in voluptate velit esse cillum dolore eu fugiat nulla pariatur. Excepteur sint occaecat cupidatat non proident, sunt in culpa qui officia deserunt mollit anim id est laborum.</p>
    <p>Lorem ipsum dolor sit amet, consectetur adipisicing elit, sed do eiusmod tempor incididunt ut labore et dolore magna aliqua. Ut enim ad minim veniam, quis nostrud exercitation ullamco laboris nisi ut aliquip ex ea commodo consequat. Duis aute irure dolor in reprehenderit in voluptate velit esse cillum dolore eu fugiat nulla pariatur. Excepteur sint occaecat cupidatat non proident, sunt in culpa qui officia deserunt mollit anim id est laborum.</p>
  </div>
  <div class="signature" role="img" aria-label="Handwritten signature of the sender"></div>
  <div class="closing">
    <p class="regards">Yours Sincerely,</p>
    <p class="signer">Elin Tarow</p>
  </div>
  <div class="foot-left">
    <p class="small">www.<span class="accent">varundelpartners</span>.com.sg</p>
    <p class="tiny">Licensed by the Financial Oversight Board of Singapore<br>RFMC licence no. QRT804217-3</p>
  </div>
  <div class="foot-right">
    <p class="small accent">VARUNDEL PARTNERS PTE LTD</p>
    <p class="tiny" style="margin-top:3px">48 Harlow Street, #09-03 Linden Plaza, Singapore 058211 &nbsp;<span class="accent">■</span> +65 6482 1907</p>
  </div>
  <div class="base-strip"></div>
</section>

<!-- Presentation folder -->
<section class="sheet folder">
  <div class="blue-field"></div>
  <svg class="ridge" viewBox="0 0 346 170" height="170" preserveAspectRatio="none" aria-hidden="true">
    <polygon points="0,14 85,0 125,24 200,29 236,56 346,0 346,170 0,170" fill="var(--slate)"/>
    <polyline points="236,56 346,0" fill="none" stroke="var(--blue-light)" stroke-width="7"/>
    <polyline points="125,24 200,29 236,56" fill="none" stroke="var(--blue-light)" stroke-width="4"/>
  </svg>
  <div class="brand-name on-blue">Varundel Partners</div>
</section>

<!-- Business card front -->
<section class="sheet card-front">
  <div class="brand-name">Varundel Partners</div>
  <div class="person">
    <p class="name">NORA KELL</p>
    <p class="tiny">CEO &amp; Founder</p>
  </div>
  <div class="address">
    <p class="tiny">48 Harlow Street, #09-03 Linden Plaza<br>Singapore 058211</p>
  </div>
  <div class="contact">
    <p class="tiny">+65 6482 1907 <span class="accent">■</span><br>info@varundelpartners.com <span class="accent">■</span></p>
  </div>
  <div class="base-strip"></div>
</section>

<!-- Business card back -->
<section class="sheet card-back">
  <div class="blue-field"></div>
  <svg class="ridge" viewBox="0 0 133 40" height="40" preserveAspectRatio="none" aria-hidden="true">
    <polygon points="0,12 30,4 48,14 80,16 95,26 133,2 133,40 0,40" fill="var(--slate)"/>
    <polyline points="95,26 133,2" fill="none" stroke="var(--blue-light)" stroke-width="3"/>
  </svg>
  <div class="brand-name on-blue">Varundel Partners</div>
</section>

<!-- DL letter -->
<section class="sheet dl-letter">
  <div class="brand-name">Varundel Partners</div>
  <div class="foot-left">
    <p class="small accent">VARUNDEL PARTNERS PTE LTD</p>
    <p class="tiny" style="margin-top:6px">48 Harlow Street, #09-03 Linden Plaza, Singapore 058211 &nbsp;<span class="accent">■</span> +65 6482 1907</p>
  </div>
  <div class="foot-right">
    <p class="small">www.<span class="accent">varundelpartners</span>.com.sg</p>
    <p class="tiny">Licensed by the Financial Oversight Board of Singapore<br>RFMC licence no. QRT804217-3</p>
  </div>
  <div class="base-strip"></div>
</section>

<!-- Envelope -->
<section class="sheet envelope">
  <div class="flap"></div>
  <div class="brand-name on-blue">Varundel Partners</div>
</section>

<!-- CD sleeve -->
<section class="sheet cd-sleeve">
  <div class="blue-field"></div>
  <svg class="ridge" viewBox="0 0 195 80" height="80" preserveAspectRatio="none" aria-hidden="true">
    <polygon points="0,8 42,0 68,12 110,14 126,32 195,0 195,80 0,80" fill="var(--slate)"/>
    <polyline points="126,32 195,0" fill="none" stroke="var(--blue-light)" stroke-width="5"/>
  </svg>
  <div class="brand-name on-blue">Varundel Partners</div>
</section>

<!-- CD disc -->
<svg class="cd-disc" viewBox="0 0 168 168" aria-label="Varundel Partners disc">
  <defs>
    <clipPath id="disc-shape"><circle cx="84" cy="84" r="84"/></clipPath>
  </defs>
  <g clip-path="url(#disc-shape)">
    <rect width="168" height="168" fill="var(--paper)"/>
    <polygon points="0,104 30,108 52,112 84,116 104,130 168,96 168,168 0,168" fill="var(--blue)"/>
    <polygon points="0,110 30,114 52,118 84,122 104,136 168,102 168,168 0,168" fill="var(--slate)"/>
  </g>
  <circle cx="84" cy="84" r="84" fill="none" stroke="#dcdcdc" stroke-width="1"/>
  <text x="48" y="38" font-family="Mulish, Arial, sans-serif" font-size="10" font-weight="700" fill="var(--blue-deep)">Varundel Partners</text>
  <circle cx="84" cy="84" r="24" fill="#e7e7e7" stroke="#cfcfcf"/>
  <circle cx="84" cy="84" r="14" fill="#d6d6d6" stroke="#c4c4c4"/>
  <circle cx="84" cy="84" r="7" fill="var(--bg)"/>
</svg>

<!-- Compliments slip -->
<section class="sheet compliments">
  <div class="brand-name">Varundel Partners</div>
  <p class="greeting">With <b>Compliments</b></p>
  <div class="foot-left">
    <p class="tiny">48 Harlow Street, #09-03 Linden Plaza, Singapore 058211 &nbsp;<span class="accent">■</span> +65 6482 1907</p>
  </div>
  <div class="foot-right">
    <p class="small">www.<span class="accent">varundelpartners</span>.com.sg</p>
    <p class="tiny">Licensed by the Financial Oversight Board of Singapore<br>RFMC licence no. QRT804217-3</p>
  </div>
  <div class="base-strip"></div>
</section>

</body>
</html>
```